Velmora Responsive Website Redesign

We need a web site design for our music marketing company. We provide musicians, artists, rappers, records labels a way to help them market an promote there music.

PLEASE NOTE THE BOOTSTRAP THEME WE ARE USING
PLEASE NOTE THE WIREFRAME FOR THE PAGES I HAVE INCLUDED
WE ARE LOOKING FOR THE DASHBOARD PAGE, BUT IF YOU HAVE TIME and WANT TO SHOW US A CONCEPT FOR THIS HOME PAGE. PLEASE DO (see home.jpg)

This site will will allow artists to register, upload their music, create a profile and then promote their music across our various mobile and social properties.

Here is the bootstrap theme we are planning to use. This page is something like what the artists should see when they login

http://quortexthemes.net/palvane_panel-v4.1/

Here are some examples of sites we like (look and feel):

www.brelvox.com (music site, edgy, dark colors, great consumer site for music)
yarmeo.com (clean design, easy to get around)
tundravox.com (leading artists upload site)
plimbo.com (great navigation and site leads the user to an end point --> invest money)

I would like to see your design skills to make this theme. I have uploaded the homepage and the logged in page. Remember this is a responsive site, so the webpage should be designed with that intention.

I have provide files (wireframes) to give you direction on some possibilities for the design you are creating.

dashboard.jpg - this page is what the artists will see when he logs in. the homepage is very simple so this is not something that I will ask you do design now.

History
Here is some history about our business:
1. Founded in 2002
2. Our last site was more of a social marketing site that registered about 20,000 artists
3. That site didn't make any money and it was costly to maintain
4. Artists registered for free and not many signed up for our premium services
5. We offered a lot of different services and weren't really good at anyone thing for artists.

To see an old version of our site go here:
https://oldpages.example.org/snap/20150207122208/http://www.velmora.biz/

Its because of this that we shut the site down and decided to redesign it

Next Steps
A. Design Build a better website
B. Have the website that sells 1 or 2 things, and do that better than any other site
C. Focus on registering artists, offering them services that they want, and make it easy for them to find these services once they are in our site.

Other items
200,000 facebook likes (www.friendloop.example/velmorabiz)
85,000 Twitter followers (www.friendloop.example/velmroa)

Files I have provided:
Content - there is no content at this point
Updates

Please note this project is to redesign velmora.biz using the information I provided in the brief. WE ARE NOT REDESIGNING THE WORDRPESS SITE (velmora.hostquill.net). This site is only to be used for getting the logo. WE ARE BUILDING A NEW Website for velmora.biz. I have provided:1. Wiresframes of what is neede (see dashboard.jpg)2. A link to the bootstrap theme we will be usingPlease review the brief again. I DO LIKE YOUR DESIGNS. Its just not what this project is for. Petra Added Thursday, October 1, 2015

Target Market(s)

Musician,
Records Labels,
Indie Artists
Unsigned Artists / Bands

Industry/Entity Type

Artists

Number of Pages Required

2 page

Font styles to use
Other font styles liked:
• Google Lato or Helvetica,

Requirements
Must have
• We are using a theme (see the brief above), but the site should have its own distinct look and feel
• Clear navigation (big buttons, and call to actions)
• The site should focus on driving member to register and by services from us

```html
<!DOCTYPE html>
<html lang="en">
<head>
<meta charset="utf-8">
<title>Velmora Artist Dashboard</title>
<link href="https://fonts.googleapis.com/css2?family=Lato:wght@300;400;700;900&display=swap" rel="stylesheet">
<style>
:root{
  --sidebar:#2c353e;
  --sidebar-dark:#232a31;
  --sidebar-active:#8fa6b5;
  --topbar:#3d5566;
  --blue:#1e8fd6;
  --orange:#e1622a;
  --green:#5cb85c;
  --yellow:#e9c23a;
  --purple:#8e6bd6;
  --text:#4a4f55;
  --muted:#9aa1a8;
  --line:#e3e6e9;
  --band:#dcdfe2;
  --card:#3a3f45;
  --footer:#2a3138;
  --white:#ffffff;
}
*{box-sizing:border-box;margin:0;padding:0}
html,body{width:878px;height:1200px;overflow:hidden}
body{font-family:'Lato',Helvetica,Arial,sans-serif;color:var(--text);background:var(--white);position:relative}

/* sidebar */
.sidebar{position:absolute;left:0;top:0;width:180px;height:1157px;background:var(--sidebar)}
.brand{height:58px;background:var(--topbar);display:flex;align-items:center;gap:8px;padding-left:14px;color:var(--white);font-weight:900;font-size:19px}
.brand-dot{width:14px;height:14px;border-radius:50%;background:var(--blue)}
.profile{display:flex;gap:8px;padding:14px 12px;align-items:center}
.avatar{width:40px;height:44px;background:linear-gradient(#8b8f93,#4e5257)}
.profile-name{color:var(--white);font-size:11px;font-weight:700}
.profile-role{color:var(--muted);font-size:9px;margin-top:2px}
.menu{list-style:none}
.menu-head{display:flex;align-items:center;gap:7px;font-size:10.5px;font-weight:700;padding:9px 14px 5px;letter-spacing:.3px}
.menu-head.active{background:var(--sidebar-active);color:var(--white);padding:10px 14px;margin-bottom:6px}
.menu-head i{width:9px;height:9px;border-radius:2px;background:currentColor;display:block}
.menu-item{font-size:9.5px;color:#c4cad0;padding:3px 0 3px 30px}
.menu-item::before{content:"";display:inline-block;width:4px;height:4px;background:#6f7b86;margin-right:6px;vertical-align:middle}
.c-green{color:var(--green)}.c-orange{color:var(--orange)}.c-blue{color:var(--blue)}.c-yellow{color:var(--yellow)}.c-purple{color:var(--purple)}

/* top nav */
.topbar{position:absolute;left:180px;top:0;width:698px;height:58px;background:var(--topbar);display:flex;justify-content:space-around;align-items:center}
.topbar a{color:#d6dee4;font-size:10px;text-decoration:none;letter-spacing:.5px}

/* notification */
.notice{position:absolute;left:180px;top:58px;width:698px;height:192px;background:linear-gradient(135deg,#4d6a78,#7d96a1 55%,#b4c2c8)}
.notice h1{position:absolute;left:36px;top:30px;color:var(--white);font-weight:400;font-size:22px;letter-spacing:1px}
.notice p{position:absolute;left:36px;top:76px;width:600px;color:#e3eaee;font-size:10px;line-height:1.5}
.btn{display:inline-flex;align-items:center;justify-content:center;color:var(--white);font-size:11px;height:30px;padding:0 16px;border-radius:2px}
.btn-dark{background:#3b4248}
.btn-blue{background:var(--blue)}
.btn-orange{background:var(--orange)}
.notice .actions{position:absolute;left:36px;top:130px;display:flex;gap:14px}

/* content rows */
.row-title{position:absolute;left:212px;font-size:17px}
.progress-title{top:298px;color:var(--orange)}
.progress{position:absolute;left:212px;top:348px;width:604px;height:12px;background:#cfd4d8}
.progress span{display:block;width:46%;height:100%;background:var(--blue)}
.progress-labels{position:absolute;left:212px;top:366px;width:604px;display:flex;justify-content:space-between;font-size:9px;color:var(--blue)}
.progress-labels span:last-child{color:var(--muted)}
.divider{position:absolute;left:180px;width:698px;height:1px;background:var(--line)}
.upload-title{top:500px;color:var(--blue)}

/* metrics */
.metrics{position:absolute;left:200px;top:562px;width:660px;height:186px;background:linear-gradient(135deg,#263745,#3b5a6e 50%,#1e2b35)}
.metrics h2{position:absolute;left:12px;top:10px;color:var(--white);font-size:15px;font-weight:700}
.songs{position:absolute;left:12px;top:44px;list-style:none}
.songs li{display:flex;align-items:center;gap:6px;color:var(--white);font-size:8.5px;margin-bottom:7px}
.songs b{display:inline-block;height:5px;background:#cfd7dc}
.songs em{font-style:normal;color:var(--yellow)}
.metrics .btn{position:absolute;left:12px;top:146px;height:26px;font-size:10px}
.chart{position:absolute;left:330px;top:30px}

/* market */
.market-art{position:absolute;left:212px;top:786px;width:240px;height:146px;background:radial-gradient(circle at 50% 55%,#f0a03a,#b3321b 45%,#1a1212 85%);box-shadow:0 2px 5px rgba(0,0,0,.3)}
.market-title{position:absolute;left:484px;top:810px;color:var(--blue);font-size:15px}
.market-cta{position:absolute;left:484px;top:846px;width:300px;height:34px;font-size:10.5px}

/* services band */
.band{position:absolute;left:180px;top:952px;width:698px;height:205px;background:var(--band)}
.card{position:absolute;top:30px;width:186px;height:150px;background:var(--card);box-shadow:0 2px 4px rgba(0,0,0,.35);display:flex;flex-direction:column;align-items:center;justify-content:flex-end;padding-bottom:16px;gap:22px}
.card span{color:#dfe3e6;font-size:10px}

/* footer */
.footer{position:absolute;left:0;top:1157px;width:878px;height:43px;background:var(--footer);display:flex;align-items:center;padding:0 18px;font-size:9px;color:#aeb5bb}
.footer nav{display:flex;gap:24px}
.footer .copy{margin-left:auto;margin-right:22px}
.social{display:flex;gap:6px;align-items:center}
.social i{width:16px;height:16px;border-radius:50%;display:block}
</style>
</head>
<body>

<aside class="sidebar">
  <div class="brand"><span class="brand-dot"></span>Velmora</div>
  <div class="profile">
    <div class="avatar" role="img" aria-label="Artist profile photo"></div>
    <div><div class="profile-name">Rae Calloway</div><div class="profile-role">MARKETING ARTIST</div></div>
  </div>
  <ul class="menu">
    <li class="menu-head active"><i></i>DASHBOARD</li>
    <li class="menu-head c-green"><i></i>MY PROFILE</li>
    <li class="menu-item">Profile</li><li class="menu-item">Biography</li><li class="menu-item">Social Links</li><li class="menu-item">Payment History</li>
    <li class="menu-head c-orange"><i></i>MARKET &amp; PROMOTE</li>
    <li class="menu-item">Create New Campaign</li><li class="menu-item">View Existing Campaigns</li>
    <li class="menu-head c-blue"><i></i>MY MUSIC</li>
    <li class="menu-item">Upload</li><li class="menu-item">Manage</li>
    <li class="menu-head c-green"><i></i>MY VIDEOS</li>
    <li class="menu-item">Upload</li><li class="menu-item">Manage</li>
    <li class="menu-head c-yellow"><i></i>SETTINGS</li>
    <li class="menu-head c-purple"><i></i>LOGOUT</li>
  </ul>
</aside>

<nav class="topbar"><a>Home</a><a>Services</a><a>Artists</a><a>Blog</a><a>Contact Us</a></nav>

<section class="notice" role="img" aria-label="Blurred studio photo behind notification">
  <h1>NOTIFICATION</h1>
  <p>Your artist account is almost ready. Finish the remaining steps below to unlock campaigns, promotion tools and detailed reports for every song and video you upload to your profile.</p>
  <div class="actions"><span class="btn btn-dark">Close This Message</span><span class="btn btn-blue">Proceed to Next Step</span></div>
</section>

<h2 class="row-title progress-title">Almost Here! Please Complete Your Profile .</h2>
<div class="progress"><span></span></div>
<div class="progress-labels"><span>0%</span><span>Almost</span><span>Awesome</span></div>
<span class="btn btn-orange" style="position:absolute;left:656px;top:408px;width:160px">Update Your Profile</span>
<div class="divider" style="top:468px"></div>

<h2 class="row-title upload-title">Let's Upload Your Songs, and Videos (3)</h2>
<span class="btn btn-blue" style="position:absolute;left:656px;top:494px;width:160px">&#8679;&nbsp; Upload Music</span>
<div class="divider" style="top:550px"></div>

<section class="metrics" role="img" aria-label="Performance and metrics panel over concert photo">
  <h2>Performance &amp; Metrics</h2>
  <ul class="songs">
    <li>Song 1 Name <b style="width:70px"></b><em>120</em></li>
    <li>Song 2 Name <b style="width:50px"></b><em>86</em></li>
    <li>Song 3 Name <b style="width:36px"></b><em>54</em></li>
  </ul>
  <span class="btn btn-blue">View All</span>
  <svg class="chart" width="200" height="140" viewBox="0 0 200 140">
    <g fill="#e8edf0">
      <rect x="10" y="100" width="22" height="30"/><rect x="44" y="82" width="22" height="48"/>
      <rect x="78" y="64" width="22" height="66"/><rect x="112" y="44" width="22" height="86"/>
      <rect x="146" y="20" width="22" height="110"/>
    </g>
    <polyline points="8,96 50,72 88,60 124,34 172,10" fill="none" stroke="#ffffff" stroke-width="3"/>
    <path d="M172 10 l-10 2 l6 7z" fill="#ffffff"/>
    <line x1="0" y1="132" x2="190" y2="132" stroke="#cfd7dc" stroke-width="2"/>
  </svg>
</section>

<div class="market-art" role="img" aria-label="Glowing music artwork"></div>
<h2 class="market-title">Market &amp; Promote Your Music Now</h2>
<span class="btn btn-blue market-cta">Now, let's getting people talking about your music</span>

<section class="band">
  <div class="card" style="left:34px">
    <svg width="60" height="48" viewBox="0 0 60 48" fill="#ffffff"><path d="M4 16h10l26-14v44L14 32H4z"/><rect x="12" y="32" width="8" height="14"/><path d="M46 14l10-6M46 24h12M46 34l10 6" stroke="#fff" stroke-width="3"/></svg>
    <span>Velmora Services Promo</span>
  </div>
  <div class="card" style="left:256px">
    <svg width="60" height="52" viewBox="0 0 60 52" fill="none" stroke="#ffffff" stroke-width="6"><circle cx="22" cy="30" r="10" stroke-dasharray="6 3"/><circle cx="44" cy="14" r="7" stroke-width="5" stroke-dasharray="4 2"/></svg>
    <span>Manage Your Setting</span>
  </div>
  <div class="card" style="left:478px">
    <svg width="54" height="54" viewBox="0 0 54 54" fill="#ffffff"><path d="M28 4h22v22L24 52 2 30z"/><circle cx="40" cy="14" r="4" fill="#3a3f45"/></svg>
    <span>Complete Promo</span>
  </div>
</section>

<footer class="footer">
  <nav><span>Home</span><span>Main</span><span>Blog</span><span>Contact</span></nav>
  <span class="copy">Velmora &copy; 2015 | Privacy Policy</span>
  <span style="margin-right:8px">FOLLOW US</span>
  <div class="social"><i style="background:#3b5998"></i><i style="background:#1da1f2"></i><i style="background:#dd4b39"></i><i style="background:#e1622a"></i><i style="background:#0077b5"></i></div>
</footer>

</body>
</html>
```